CFO services graphic design

I own a business consulting firm called Hollins Advisory and we need a graphic for CFO services in our colours and branding. The attached file "CFO services to be put into Hollins advisory theme", shows the content for the design. The two other files show the theme and colours for the new design.

```html
<!DOCTYPE html>
<html lang="en">
<head>
<meta charset="utf-8">
<title>Chief Financial Officer Services</title>
<link rel="stylesheet" href="https://fonts.googleapis.com/css2?family=League+Spartan:wght@500;600&family=Poppins:wght@400&display=swap">
<style>
  :root {
    --sky: #5ec8f8;
    --amber: #f0912e;
    --ink-blue: #1d3a4b;
    --ink-amber: #3b2412;
    --ring-1: #f1f2f4;
    --ring-2: #e8e9eb;
    --ring-3: #e0e1e3;
    --halo: #f3f4f6;
    --paper: #ffffff;
  }
  html, body { margin: 0; padding: 0; overflow: hidden; background: var(--paper); }
  .canvas { width: 1168px; height: 1200px; display: block; }
  .service-title { font-family: "League Spartan", sans-serif; font-weight: 500; font-size: 18.5px; text-anchor: middle; letter-spacing: .2px; }
  .on-sky { fill: var(--ink-blue); }
  .on-amber { fill: var(--ink-amber); }
  .service-note { font-family: "Poppins", sans-serif; font-size: 11px; text-anchor: middle; }
  .hub-title { font-family: "League Spartan", sans-serif; font-weight: 600; font-size: 30px; fill: var(--ink-blue); text-anchor: middle; }
  .icon { fill: none; stroke: #fff; stroke-width: 2; stroke-linecap: round; stroke-linejoin: round; }
  .icon-fill { fill: #fff; stroke: none; }
  .icon-dollar { font-family: "Poppins", sans-serif; font-size: 13px; fill: #fff; text-anchor: middle; }
</style>
</head>
<body>
<svg class="canvas" viewBox="0 0 1168 1200" xmlns="http://www.w3.org/2000/svg" role="img" aria-label="Chief Financial Officer services wheel">
  <defs>
    <g id="node-sky">
      <circle r="110" fill="var(--halo)"/>
      <circle r="100" fill="var(--paper)" stroke="var(--amber)" stroke-width="2"/>
      <circle r="100" fill="none" stroke="var(--sky)" stroke-width="2.2" stroke-dasharray="314 314"/>
      <circle r="89" fill="var(--sky)"/>
    </g>
    <g id="node-amber">
      <circle r="110" fill="var(--halo)"/>
      <circle r="100" fill="var(--paper)" stroke="var(--sky)" stroke-width="2"/>
      <circle r="100" fill="none" stroke="var(--amber)" stroke-width="2.2" stroke-dasharray="314 314"/>
      <circle r="89" fill="var(--amber)"/>
    </g>
  </defs>

  <g class="backdrop">
    <circle cx="596" cy="601" r="362" fill="var(--ring-1)"/>
    <circle cx="596" cy="601" r="292" fill="var(--ring-2)"/>
    <circle cx="596" cy="601" r="237" fill="var(--ring-3)"/>
  </g>

  <g class="connectors" stroke-width="2">
    <line x1="596" y1="601" x2="596" y2="351" stroke="var(--sky)"/>
    <line x1="596" y1="601" x2="774" y2="424" stroke="var(--amber)"/>
    <line x1="596" y1="601" x2="848" y2="601" stroke="var(--sky)"/>
    <line x1="596" y1="601" x2="774" y2="779" stroke="var(--amber)"/>
    <line x1="596" y1="601" x2="596" y2="853" stroke="var(--sky)"/>
    <line x1="596" y1="601" x2="418" y2="779" stroke="var(--amber)"/>
    <line x1="596" y1="601" x2="344" y2="601" stroke="var(--sky)"/>
    <line x1="596" y1="601" x2="418" y2="424" stroke="var(--amber)"/>
  </g>

  <g class="hub">
    <circle cx="596" cy="601" r="182" fill="#eef2fb"/>
    <circle cx="596" cy="601" r="172" fill="none" stroke="var(--amber)" stroke-width="2"/>
    <circle cx="596" cy="601" r="172" fill="none" stroke="var(--sky)" stroke-width="2.2" stroke-dasharray="70 200" transform="rotate(-110 596 601)"/>
    <circle cx="596" cy="601" r="162" fill="var(--sky)"/>
    <text class="hub-title" x="596" y="599">CHIEF FINANCIAL</text>
    <text class="hub-title" x="596" y="629">OFFICER SERVICES</text>
  </g>

  <g class="service" transform="translate(596 250)">
    <use href="#node-sky"/>
    <g class="icon" transform="translate(-28 -68)">
      <path d="M6 4 h28 v44 h-30 v-6"/><path d="M0 6 a4 4 0 0 1 8 0 v40 a4 4 0 0 0 4 4 h28 a4 4 0 0 0 0 -6 h-6"/>
      <path d="M12 14 h14 M12 21 h18 M12 28 h18 M12 35 h18"/>
      <circle cx="37" cy="10" r="8"/><path d="M43 16 l8 8"/>
    </g>
    <text class="icon-dollar" x="9" y="-53" font-size="11">$</text>
    <text class="service-title on-sky" x="0" y="7">COST ACCOUNTING</text>
    <text class="service-title on-sky" x="-2" y="26">&amp; COST</text>
    <text class="service-title on-sky" x="-2" y="45">MANAGEMENT</text>
    <circle cx="0" cy="101" r="6" fill="var(--sky)"/>
  </g>

  <g class="service" transform="translate(845 354)">
    <use href="#node-amber" transform="rotate(135)"/>
    <g class="icon" transform="translate(0 -40)">
      <path d="M-6 -10 h12 M-7 -5 h14"/><path d="M-6 -5 c-14 8 -18 30 6 30 c24 0 20 -22 6 -30"/>
      <circle cx="0" cy="10" r="10"/>
    </g>
    <text class="icon-dollar" x="0" y="-25">$</text>
    <text class="service-title on-amber" x="0" y="-1">CAPTIAL</text>
    <text class="service-title on-amber" x="0" y="18">STRUCTURE &amp; THE</text>
    <text class="service-title on-amber" x="-2" y="37">COST OF CAPITAL</text>
    <circle cx="-71" cy="70" r="6" fill="var(--amber)"/>
  </g>

  <g class="service" transform="translate(948 602)">
    <use href="#node-sky" transform="rotate(90)"/>
    <g class="icon" transform="translate(-20 -58)">
      <path d="M0 18 l10 -8 l9 8 l18 -16"/><path d="M30 2 h7 v7"/>
      <path d="M2 24 v10 M10 20 v14 M19 24 v10 M28 16 v18 M37 12 v22" stroke-width="4" stroke-linecap="butt"/>
    </g>
    <text class="service-title on-sky" x="0" y="-5">LONG-TERM &amp;</text>
    <text class="service-title on-sky" x="0" y="14">SHORT-TERM</text>
    <text class="service-title on-sky" x="0" y="33">INVESTMENT</text>
    <text class="service-title on-sky" x="-2" y="52">DECISIONS</text>
    <circle cx="-101" cy="0" r="6" fill="var(--sky)"/>
  </g>

  <g class="service" transform="translate(845 851)">
    <use href="#node-amber" transform="rotate(-135)"/>
    <g class="icon" transform="translate(0 -22)" stroke-width="3.5">
      <path d="M-26 6 a26 26 0 0 1 52 0"/><path d="M-2 4 l8 -14"/>
    </g>
    <text class="service-title on-amber" x="0" y="7">PERFORMANCE</text>
    <text class="service-title on-amber" x="0" y="26">EVALUATION</text>
    <circle cx="-71" cy="-71" r="6" fill="var(--amber)"/>
  </g>

  <g class="service" transform="translate(596 954)">
    <use href="#node-sky" transform="rotate(180)"/>
    <g class="icon" transform="translate(0 -42)">
      <path d="M-24 -6 a26 26 0 0 1 22 -22 v26"/><path d="M4 -26 a26 26 0 0 1 22 22 h-22 z"/>
      <path d="M26 2 a26 26 0 0 1 -26 24"/><path d="M2 2 l18 16"/>
      <circle cx="-16" cy="14" r="11"/>
    </g>
    <text class="icon-dollar" x="-16" y="-23">$</text>
    <text class="service-title on-sky" x="0" y="5">BUDGETING</text>
    <text class="service-title on-sky" x="2" y="24">&amp; STRATEGIC</text>
    <text class="service-title on-sky" x="-2" y="43">PLANNING</text>
    <circle cx="0" cy="-101" r="6" fill="var(--sky)"/>
  </g>

  <g class="service" transform="translate(347 851)">
    <use href="#node-amber" transform="rotate(-45)"/>
    <g transform="translate(0 -36)">
      <path class="icon" d="M0 -24 L26 20 H-26 Z" stroke-width="3"/>
      <rect class="icon-fill" x="-2.5" y="-10" width="5" height="18"/>
      <rect class="icon-fill" x="-2.5" y="11" width="5" height="5"/>
    </g>
    <text class="service-title on-amber" x="0" y="14">RISK</text>
    <text class="service-title on-amber" x="-2" y="33">MANAGEMENT</text>
    <circle cx="71" cy="-71" r="6" fill="var(--amber)"/>
  </g>

  <g class="service" transform="translate(244 602)">
    <use href="#node-sky" transform="rotate(-90)"/>
    <g class="icon" transform="translate(-22 -60)">
      <path d="M4 0 h22 l12 12 v14 M26 0 v12 h12"/><path d="M34 50 h-30 v-50"/>
      <path d="M10 18 h14 M10 26 h14 M10 34 h10"/>
      <path d="M40 22 l11 5 v8 c0 8 -5 12 -11 15 c-6 -3 -11 -7 -11 -15 v-8 z"/><path d="M35 36 l4 4 l7 -7"/>
    </g>
    <text class="service-title on-sky" x="0" y="13">COMPLIANCE:</text>
    <text class="service-note on-sky" x="-2" y="33">tax, legal &amp; regulatory</text>
    <circle cx="101" cy="0" r="6" fill="var(--sky)"/>
  </g>

  <g class="service" transform="translate(347 354)">
    <use href="#node-amber" transform="rotate(45)"/>
    <g class="icon" transform="translate(-28 -62)">
      <path d="M2 0 h40 v26 h-26 l-10 8 v-8 h-4 z"/><path d="M9 8 h26 M9 14 h26 M9 20 h16"/>
      <path d="M44 8 h12 v26 h-4 v8 l-10 -8 h-22 v-6"/>
    </g>
    <text class="service-title on-amber" x="0" y="-3">COMMUNICATION:</text>
    <text class="service-note on-amber" x="-4" y="15">Board of Directors,</text>
    <text class="service-note on-amber" x="0" y="29">creditors, owners, investors,</text>
    <text class="service-note on-amber" x="-3" y="43">credit rating agencies</text>
    <circle cx="71" cy="70" r="6" fill="var(--amber)"/>
  </g>
</svg>
</body>
</html>
```